Freeze dried pet treats and chews packaging design

We are an Belgium based brand selling all natural treats and chews for pets. We are looking for a full color packaging design for a new line of freeze dried treats and chews for cats and dogs. The design should look familiar for our customers with our existing logo, but with a fresh new design especially for this new line. It should reflect our core values of natural, species appropriate food products without any additives or nasties.
The packaging will be a stand-up pouch with zipper, eurohole, easy open and with a window somewhere in the design to show the products inside. Please present your design as a mockup if possible.
Name of the product will be "Velmo Freeze Dried Bitzoos". Add icons to emphasize certain aspects of the product:
- 100% natural
- freeze dried (preserves all nutrients best)
- 100% mono protein
- without additives
- high in protein
- high in flavor
The design is a generic one for 12 different products, only one pouch will be produced and finished with 12 different round labels to indicate the protein source (beef, chicken, lamb, etc). You can include one of these stickers on your design to make the example complete. The sticker should have a separate color for every protein source to make it good distinguishable, an icon representing the protein source (see examples of existing packaging) and a round text around it with the protein source in text in Dutch, French and English (example: RUND - BŒUF - BEEF).
Important: after this design we need more designs for other new product lines, so the winner might get more out of this then only this one project!
High premium pet products
Petfood
- Fontastique, Roboto (used for logo and current designs), others welcome too

```html
<!DOCTYPE html>
<html lang="en">
<head>
<meta charset="utf-8">
<title>Velmo Freeze Dried Bitzoos – Pouch Front</title>
<link href="https://fonts.googleapis.com/css2?family=Titan+One&family=Roboto:wght@400;500;700&display=swap" rel="stylesheet">
<style>
  :root{
    --bg:#e4e4e4;
    --pouch-white:#f7f7f7;
    --purple:#6a3d94;
    --purple-band:#4e2c74;
    --purple-deep:#3a1f5a;
    --green:#8dc63f;
    --slot:#808080;
    --label-red:#e2262c;
    --white:#ffffff;
  }
  html,body{margin:0;padding:0;width:1200px;height:1200px;overflow:hidden;background:var(--bg);}
  .canvas{position:relative;width:1200px;height:1200px;}
  .pouch{position:absolute;left:347px;top:245px;width:505px;height:740px;}
  .pouch svg{display:block;}
  .brand-name{font-family:'Roboto',sans-serif;font-weight:500;font-size:52px;fill:var(--purple);}
  .title{font-family:'Titan One',sans-serif;font-size:44px;fill:var(--white);stroke:var(--purple-deep);stroke-width:5px;paint-order:stroke;letter-spacing:1px;}
  .feature-label{font-family:'Roboto',sans-serif;font-size:11.5px;fill:var(--white);}
  .feature-note{font-family:'Roboto',sans-serif;font-size:5.5px;fill:var(--white);}
  .icon-ring{fill:none;stroke:var(--white);stroke-width:1.6;}
  .icon-inner{fill:var(--white);opacity:.95;}
  .icon-glyph{fill:none;stroke:var(--purple);stroke-width:1.4;stroke-linecap:round;stroke-linejoin:round;}
  .sticker-text{font-family:'Roboto',sans-serif;font-weight:700;font-size:8.4px;fill:var(--white);letter-spacing:.6px;}
</style>
</head>
<body>
<div class="canvas">
  <div class="pouch">
    <svg width="505" height="740" viewBox="0 0 505 740" xmlns="http://www.w3.org/2000/svg">
      <defs>
        <clipPath id="pouch-shape">
          <path d="M14 0 H491 Q505 0 505 14 V726 Q505 740 491 740 H14 Q0 740 0 726 V14 Q0 0 14 0 Z"/>
        </clipPath>
        <linearGradient id="window-fill" x1="0" y1="0" x2="1" y2="1">
          <stop offset="0" stop-color="#9c9c9c"/>
          <stop offset=".45" stop-color="#c8c8c8"/>
          <stop offset="1" stop-color="#8f8f8f"/>
        </linearGradient>
        <path id="sticker-ring" d="M256 667 a34 34 0 1 1 0.01 0"/>
      </defs>

      <g clip-path="url(#pouch-shape)">
        <rect class="pouch-body" width="505" height="740" fill="var(--pouch-white)"/>
        <!-- purple lower field -->
        <path class="purple-field" d="M0 250 Q150 300 505 222 V740 H0 Z" fill="var(--purple)"/>
        <!-- green swoosh -->
        <path class="green-swoosh" d="M0 225 Q120 290 260 240 Q360 205 460 215 Q350 215 260 248 Q140 300 0 255 Z" fill="var(--green)"/>
        <!-- feature band -->
        <rect class="feature-band" x="0" y="424" width="505" height="103" fill="var(--purple-band)"/>
        <!-- product window -->
        <path role="img" aria-label="Clear window showing the freeze dried beef treats inside" d="M52 534 H455 V620 Q455 690 254 690 Q52 690 52 620 Z" fill="url(#window-fill)"/>
      </g>

      <!-- euro hole -->
      <rect class="euro-hole" x="215" y="20" width="81" height="15" rx="7.5" fill="var(--slot)"/>

      <!-- brand name -->
      <circle cx="178" cy="160" r="9" fill="var(--green)"/>
      <text class="brand-name" x="262" y="178" text-anchor="middle">Velmo</text>

      <!-- pet illustration -->
      <rect role="img" aria-label="Illustration of two dogs and a cat peeking over the title" x="101" y="227" width="307" height="118" rx="18" fill="#d9b58c" opacity=".85"/>

      <!-- title -->
      <text class="title" x="252" y="378" text-anchor="middle">FREEZE DRIED</text>
      <text class="title" x="252" y="416" text-anchor="middle">BITZOOS</text>

      <!-- feature icons -->
      <g class="feature natural" transform="translate(87 461)">
        <circle class="icon-ring" r="20"/><circle class="icon-inner" r="16.5"/>
        <path class="icon-glyph" d="M-7 7 Q-8 -7 7 -8 Q8 6 -7 7 Z M-7 7 L3 -3"/>
      </g>
      <g class="feature freeze-dried" transform="translate(149 461)">
        <circle class="icon-ring" r="20"/><circle class="icon-inner" r="16.5"/>
        <path class="icon-glyph" d="M0 -10 V4 M-6 -6 L6 2 M6 -6 L-6 2"/>
        <path class="icon-glyph" d="M0 6 Q-3 10 0 12 Q3 10 0 6 Z"/>
      </g>
      <g class="feature mono-protein" transform="translate(220 461)">
        <circle class="icon-ring" r="20"/><circle class="icon-inner" r="16.5"/>
        <circle class="icon-glyph" cy="-3" r="7"/>
        <path class="icon-glyph" d="M-4 3 L-6 11 L-2 9 L0 12 M4 3 L6 11 L2 9"/>
      </g>
      <g class="feature no-additives" transform="translate(300 461)">
        <circle class="icon-ring" r="20"/><circle class="icon-inner" r="16.5"/>
        <circle class="icon-glyph" r="10"/>
        <path class="icon-glyph" d="M-7 -7 L7 7"/>
      </g>
      <g class="feature high-protein" transform="translate(370 461)">
        <circle class="icon-ring" r="20"/><circle class="icon-inner" r="16.5"/>
        <path class="icon-glyph" d="M-8 -3 a3 3 0 1 1 4 -3 L4 4 a3 3 0 1 1 3 4 a3 3 0 1 1 -4 3 L-5 0 a3 3 0 1 1 -3 -3 Z"/>
      </g>
      <g class="feature high-flavor" transform="translate(428 461)">
        <circle class="icon-ring" r="20"/><circle class="icon-inner" r="16.5"/>
        <path class="icon-glyph" d="M-10 2 H10 Q9 10 0 10 Q-9 10 -10 2 Z"/>
        <path class="icon-glyph" d="M-4 -2 Q-6 -5 -4 -8 M0 -2 Q-2 -5 0 -9 M4 -2 Q2 -5 4 -8"/>
      </g>

      <g class="feature-labels" text-anchor="middle">
        <text class="feature-label" x="87" y="496">100%</text>
        <text class="feature-label" x="87" y="509">NATURAL</text>
        <text class="feature-label" x="149" y="496">FREEZE</text>
        <text class="feature-label" x="149" y="509">DRIED</text>
        <text class="feature-note" x="149" y="516">(preserves all</text>
        <text class="feature-note" x="149" y="522">nutrients best)</text>
        <text class="feature-label" x="220" y="496">100% MONO</text>
        <text class="feature-label" x="220" y="509">PROTEIN</text>
        <text class="feature-label" x="300" y="496">WITHOUT</text>
        <text class="feature-label" x="300" y="509">ADDITIVES</text>
        <text class="feature-label" x="370" y="496">HIGH IN</text>
        <text class="feature-label" x="370" y="509">PROTEIN</text>
        <text class="feature-label" x="428" y="496">HIGH IN</text>
        <text class="feature-label" x="428" y="509">FLAVOR</text>
      </g>

      <!-- protein source sticker -->
      <g class="protein-sticker">
        <circle cx="256" cy="633" r="43" fill="var(--label-red)"/>
        <circle cx="256" cy="633" r="26" fill="none" stroke="var(--white)" stroke-width="1.6"/>
        <text class="sticker-text"><textPath href="#sticker-ring">RUND • BŒUF • BEEF • RUND • BŒUF • BEEF •</textPath></text>
        <path d="M244 628 Q246 619 258 620 Q270 621 268 631 Q266 640 256 642 Q247 644 245 637 Z" fill="none" stroke="var(--white)" stroke-width="1.6" stroke-linejoin="round"/>
        <circle cx="251" cy="631" r="3" fill="none" stroke="var(--white)" stroke-width="1.4"/>
      </g>
    </svg>
  </div>
</div>
</body>
</html>
```